Fernhollow Estates Cards and Letterhead
EPS and PNG formatted logo files have been uploaded
Please feel free to post ideas for letterhead / stationary as well. Thanks.
SiteAdmin - I haven't yet received my logo files. If there is somewhere I can download them from please let me know. Thanks.
Attention Project Holder!!
Please be advised to upload your logo file in AI, EPS or PNG format so that the designers can incorporate your logo in this designs.
QT/PWF/HR Team
If you have the ability to create a couple of PowerPoint master slides based on the look and feel of the logo I'd be willing to pay extra for those. Thx.

```html
<!DOCTYPE html>
<html lang="en">
<head>
<meta charset="utf-8">
<title>Fernhollow Estates – Business Card</title>
<link href="https://fonts.googleapis.com/css2?family=Open+Sans:wght@400;600;700&display=swap" rel="stylesheet">
<style>
  :root{
    --bg:#e4e6e8;
    --navy:#2b3f86;
    --green:#3f9a3c;
    --green-dark:#2f7d2e;
    --green-light:#5db552;
    --grey:#6d6f73;
    --white:#ffffff;
  }
  *{margin:0;padding:0;box-sizing:border-box}
  html,body{width:1200px;height:871px;overflow:hidden}
  body{background:var(--bg);font-family:"Open Sans",Arial,sans-serif;display:flex;align-items:center;justify-content:center;gap:44px}
  .card{width:540px;height:308px;position:relative;overflow:hidden;box-shadow:0 10px 28px rgba(0,0,0,.18)}

  /* back */
  .card-back{background:linear-gradient(135deg,var(--green-light),var(--green) 55%,var(--green-dark));color:var(--white)}
  .back-brand{position:absolute;left:0;right:0;top:112px;text-align:center}
  .back-brand .brand-name{font-weight:600;font-size:30px;letter-spacing:2px;text-transform:uppercase}
  .back-brand .brand-suffix{font-weight:600;font-size:18px;letter-spacing:2px;margin-top:2px}
  .back-web{position:absolute;left:0;right:0;bottom:30px;text-align:center;font-size:14px;letter-spacing:1px}

  /* front */
  .card-front{background:var(--white)}
  .logo{position:absolute;left:130px;top:38px;width:370px}
  .logo-row{display:flex;align-items:center;gap:10px}
  .logo-square{width:22px;height:22px;background:var(--navy)}
  .logo-name{font-weight:600;font-size:25px;color:var(--navy);letter-spacing:1px;text-transform:uppercase;white-space:nowrap}
  .logo-rule{height:2px;background:var(--green);margin:4px 44px 0 32px}
  .logo-suffix{text-align:right;font-weight:600;font-size:20px;color:var(--navy);letter-spacing:1px;margin-top:-2px}

  .person{position:absolute;left:140px;top:126px;text-align:right;width:140px}
  .person-name{font-weight:700;font-size:15px;color:var(--navy)}
  .person-title{font-size:11px;color:var(--grey);margin-top:2px}
  .address{position:absolute;left:40px;top:178px;font-size:10.5px;color:var(--grey);line-height:1.5}

  .contacts{position:absolute;left:304px;top:124px;list-style:none}
  .contacts li{display:flex;align-items:center;gap:8px;font-size:11px;color:var(--grey);height:19px;white-space:nowrap}
  .contacts svg{width:12px;height:12px;fill:var(--navy);flex:none}

  .footer{position:absolute;left:0;bottom:0;width:100%;height:64px}
  .footer svg{position:absolute;inset:0}
  .footer-web{position:absolute;right:28px;bottom:6px;font-size:13px;color:var(--white);letter-spacing:.5px}
</style>
</head>
<body>

<section class="card card-back" aria-label="Card back">
  <div class="back-brand">
    <div class="brand-name">Fernhollow Estates</div>
    <div class="brand-suffix">LLC</div>
  </div>
  <div class="back-web">www.fernhollowestates.com</div>
</section>

<section class="card card-front" aria-label="Card front">
  <div class="logo">
    <div class="logo-row">
      <span class="logo-square"></span>
      <span class="logo-name">Fernhollow Estates</span>
    </div>
    <div class="logo-rule"></div>
    <div class="logo-suffix">LLC</div>
  </div>

  <div class="person">
    <div class="person-name">Dana Whitcombe</div>
    <div class="person-title">Your Job Title</div>
  </div>
  <div class="address">
    Suite 102 Street name<br>
    State, Zip 2034, Country
  </div>

  <ul class="contacts">
    <li><svg viewBox="0 0 12 12"><path d="M2.5 1h2l1 2.5-1.3 1a6 6 0 0 0 3.3 3.3l1-1.3L11 7.5v2a1.5 1.5 0 0 1-1.5 1.5A8.5 8.5 0 0 1 1 2.5 1.5 1.5 0 0 1 2.5 1z"/></svg>555 210 4481</li>
    <li><svg viewBox="0 0 12 12"><path d="M3.5 0h5a1 1 0 0 1 1 1v10a1 1 0 0 1-1 1h-5a1 1 0 0 1-1-1V1a1 1 0 0 1 1-1zm.5 1.5v7.5h4V1.5z"/></svg>555 210 4482</li>
    <li><svg viewBox="0 0 12 12"><path d="M3 0h5v3H3zM1 4h10v6H9v2H3v-2H1zm3 4v3h4V8z"/></svg>555 210 4483</li>
    <li><svg viewBox="0 0 12 12"><path d="M0 2h12v8H0zm1 1v.3l5 3.2 5-3.2V3z"/></svg>dana.w@fernhollowestates.com</li>
  </ul>

  <div class="footer">
    <svg viewBox="0 0 540 64" preserveAspectRatio="none">
      <polygon points="0,22 230,22 250,32 0,32" fill="#2b3f86"/>
      <polygon points="0,36 540,36 540,64 0,64" fill="#3f9a3c"/>
      <polygon points="210,36 540,36 540,64 250,64" fill="#5db552"/>
    </svg>
    <div class="footer-web">www.fernhollowestates.com</div>
  </div>
</section>

</body>
</html>
```